Fashion Company Business Card

Style// Minimalism (Less is more)
Colour// No required colour. If you use a solid colour, vigorous violet is preferred, or any other mix of fashionable patterns. Purple reference to http://cdn.pixelvantor.example/blog/Famous-Purple-Logos/11-famous-purple-logos.jpg)
Font// any matching sans serif fonts (logo is helveica neue light)
Contents// as following
- logo
- (website) www.morbelle.com
- (add) 3870 Glenwick Ave, Suite 415 Toronto ON M4T 1K8
- (Office phone) +1 416 555 0173
- (email) info@morbelle.com
- (social media logos: Facebook, Instagram, Twitter, Tumblr, Vimeo, Youtube) @Morbelle/@Morbellemedia
- (slogan)│Fashion│Art│Unique
*optional - QR code
- (personal info) For example
Tessa Korby
Founder & Creative Director
c. XXX.XXX.XXXX
Please submit jpg file for selecting, and submit a psd file for editing personal info for different employers after selected. If you need more information, please email tessakorby@morbelle.com.

```html
<!DOCTYPE html>
<html lang="en">
<head>
<meta charset="utf-8">
<title>Morbelle Business Card</title>
<link rel="stylesheet" href="https://fonts.googleapis.com/css2?family=Lato:wght@300;400;700&display=swap">
<style>
  :root {
    --violet: #3b2162;
    --violet-text: #3d2466;
    --paper: #ffffff;
    --ink: #3a3a3a;
    --muted: #a9a4a6;
    --rule: #cfcfd4;
    --backdrop: #e9e9ec;
  }
  * { box-sizing: border-box; margin: 0; padding: 0; }
  html, body {
    width: 1200px; height: 926px; overflow: hidden;
    background: var(--backdrop);
    font-family: "Lato", "Helvetica Neue", Arial, sans-serif;
  }
  .canvas {
    position: relative; width: 1200px; height: 926px;
  }
  .card {
    position: absolute; left: 250px; width: 700px; height: 400px;
    box-shadow: 0 6px 18px rgba(0,0,0,.18);
  }
  /* Back of card */
  .card-back { top: 42px; background: var(--violet); color: var(--paper); }
  .card-back .brand {
    position: absolute; top: 138px; left: 0; right: 0; text-align: center;
    font-weight: 300; font-size: 78px; letter-spacing: 4px; line-height: 1;
  }
  .card-back .web {
    position: absolute; top: 240px; left: 0; right: 0; text-align: center;
    font-weight: 400; font-size: 17px; letter-spacing: 7px;
  }
  /* Front of card */
  .card-front { top: 484px; background: var(--paper); color: var(--ink); }
  .card-front .brand {
    position: absolute; left: 40px; top: 172px; width: 240px;
    font-weight: 300; font-size: 40px; letter-spacing: 2px; color: var(--violet-text);
    line-height: 1;
  }
  .divider {
    position: absolute; left: 296px; top: 40px; bottom: 40px; width: 1px; background: var(--rule);
  }
  .details { position: absolute; left: 322px; top: 40px; right: 24px; }
  .person-name {
    font-size: 31px; font-weight: 300; color: var(--violet-text); letter-spacing: .5px; line-height: 1.05;
  }
  .person-name strong { font-weight: 700; }
  .person-title {
    font-size: 13px; font-weight: 400; text-transform: uppercase; letter-spacing: .6px; margin-top: 2px;
  }
  .line { display: flex; align-items: center; gap: 7px; font-size: 15px; line-height: 1.45; }
  .line.mobile { font-size: 19px; margin-top: 3px; }
  .address { font-size: 14.5px; margin: 12px 0 6px; }
  .icon { width: 13px; height: 13px; flex: none; }
  .social { display: flex; align-items: center; gap: 5px; margin-top: 24px; font-size: 15px; }
  .social .dot { width: 17px; height: 17px; border-radius: 50%; background: var(--muted); flex: none; }
  .social .handles { margin-left: 8px; }
</style>
</head>
<body>
<div class="canvas">
  <section class="card card-back">
    <div class="brand">MORBELLE</div>
    <div class="web">WWW.MORBELLE.COM</div>
  </section>

  <section class="card card-front">
    <div class="brand">MORBELLE</div>
    <div class="divider"></div>
    <div class="details">
      <div class="person-name">TESSA <strong>KORBY</strong></div>
      <div class="person-title">Founder &amp; Creative Director</div>
      <div class="line mobile">
        <svg class="icon" viewBox="0 0 13 13" aria-hidden="true"><rect x="3" y="0.5" width="7" height="12" rx="1.3" fill="none" stroke="#3b2162" stroke-width="1.4"/><circle cx="6.5" cy="10.3" r=".8" fill="#3b2162"/></svg>
        012 555 0190
      </div>
      <div class="address">3870 Glenwick Ave, Suite 415 Toronto ON M4T 1K8</div>
      <div class="line">
        <svg class="icon" viewBox="0 0 13 13" aria-hidden="true"><rect width="13" height="13" fill="#3b2162"/><path d="M3 10 L10 3 M6 3 H10 V7" stroke="#fff" stroke-width="1.3" fill="none"/></svg>
        www.morbelle.com
      </div>
      <div class="line">
        <svg class="icon" viewBox="0 0 13 13" aria-hidden="true"><rect width="13" height="13" fill="#3b2162"/><path d="M3 4 Q3 3 4 3 L5 3 L6 5 L5 6 Q6 8 7 8 L8 7 L10 8 L10 9 Q10 10 9 10 Q3 10 3 4Z" fill="#fff"/></svg>
        +1 416 555 0173
      </div>
      <div class="line">
        <svg class="icon" viewBox="0 0 13 13" aria-hidden="true"><rect width="13" height="13" fill="#3b2162"/><rect x="2.5" y="3.5" width="8" height="6" fill="none" stroke="#fff" stroke-width="1"/><path d="M2.5 3.5 L6.5 7 L10.5 3.5" stroke="#fff" stroke-width="1" fill="none"/></svg>
        info@morbelle.com
      </div>
      <div class="social">
        <span class="dot"></span><span class="dot"></span><span class="dot"></span>
        <span class="dot"></span><span class="dot"></span><span class="dot"></span>
        <span class="handles">@Morbelle/@Morbellemedia</span>
      </div>
    </div>
  </section>
</div>
</body>
</html>
```